Tranvik Leasing Corp - Business Card Design

Need a new modern designed business card that is different and stands out to represent my equipment financing company. Tranvik Leasing Corp finances all types of equipment and all types of industries. We like to do equipment financing a different way by putting customers first and want our card to represent that different approach to business. I want a card that some remembers when they receive it so it sticks in their mind and makes that wow impression.

Card should have a black background so the logo stands out. It can be horizontial or vertical or a combination of both.

Front of card information is below that shows the information that would go on my card. That is where I want a different look or design to stand out. The front could be split black/orange colour so the logo could pop on black side and information on orange side with different lettering. Just outside the box thinking on the front of the card. Open to any type of design.

Back of card is below which i I like unless you have a different spin to provide or a different idea that would make the card better as I am open to anything that looks great.

Target Market(s)

Tranvik Leasing Corp deals with business owners in all industries.

Industry/Entity Type

Business

Contact Information for Business Card

Colors

Designer to choose colors to be used in the design.

Requirements
Must have
• Modern
• Different
• Stand Out
• Makes an Impression

```html
<!DOCTYPE html>
<html lang="en">
<head>
<meta charset="utf-8">
<title>Tranvik Leasing Corp – Business Card</title>
<link rel="stylesheet" href="https://fonts.googleapis.com/css2?family=Cinzel:wght@400&family=Open+Sans:wght@400;700&display=swap">
<style>
  :root {
    --ink: #060606;
    --orange: #f47b20;
    --red: #e8262b;
    --brown-top: #6e3a18;
    --brown-bottom: #7a1616;
    --panel-top: #6b3817;
    --panel-bottom: #741414;
    --seam: #2a0e06;
    --white: #ffffff;
    --page: #ffffff;
  }
  * { margin: 0; padding: 0; box-sizing: border-box; }
  html, body { width: 1200px; height: 1200px; overflow: hidden; background: var(--page); }
  .sheet { position: relative; width: 1200px; height: 1200px; }

  .card {
    position: absolute;
    top: 456px;
    width: 517px;
    height: 288px;
    background: var(--ink);
    box-shadow: 7px 7px 6px rgba(0,0,0,0.45);
    overflow: hidden;
  }
  .card--front { left: 70px; }
  .card--back { left: 617px; }

  .stripe { position: absolute; top: 0; height: 100%; }
  .stripe--flame { background: linear-gradient(to bottom, var(--orange), var(--red)); }
  .stripe--ember { background: linear-gradient(to bottom, var(--brown-top), var(--brown-bottom)); }

  .wordmark {
    font-family: "Cinzel", serif;
    font-weight: 400;
    color: var(--orange);
    text-transform: uppercase;
    text-align: center;
    line-height: 1.15;
  }
  .card--front .wordmark {
    position: absolute;
    left: 44px; right: 44px;
    top: 112px;
    font-size: 30px;
    letter-spacing: 2px;
  }
  .mark-square {
    display: block;
    width: 14px; height: 14px;
    margin: 0 auto 14px;
    background: var(--orange);
  }

  .back-brand {
    position: absolute;
    left: 19px; width: 244px;
    top: 72px;
  }
  .card--back .wordmark { font-size: 19px; letter-spacing: 1.5px; }
  .card--back .mark-square { width: 10px; height: 10px; margin-bottom: 10px; }
  .rule {
    position: absolute;
    left: 38px; width: 208px;
    top: 199px;
    height: 1px;
    background: #d9d9d9;
  }
  .web {
    position: absolute;
    left: 38px; width: 208px;
    top: 228px;
    font-family: "Open Sans", sans-serif;
    font-size: 13.4px;
    color: var(--white);
    white-space: nowrap;
  }

  .seam { position: absolute; top: 0; left: 263px; width: 10px; height: 100%; background: var(--seam); }
  .panel {
    position: absolute;
    top: 0; left: 273px; right: 8px; height: 100%;
    background: linear-gradient(to bottom, var(--panel-top), var(--panel-bottom));
    font-family: "Open Sans", sans-serif;
    color: var(--white);
    text-align: right;
    padding-right: 17px;
  }
  .person { position: absolute; right: 17px; top: 110px; }
  .person__name { font-weight: 700; font-size: 22px; letter-spacing: -0.3px; line-height: 1.1; }
  .person__role { font-size: 11.5px; letter-spacing: 3px; margin-top: 4px; margin-right: -3px; }
  .contact { position: absolute; right: 17px; top: 207px; font-size: 13.4px; line-height: 20px; }
</style>
</head>
<body>
<main class="sheet">
  <section class="card card--front" aria-label="Card front">
    <div class="stripe stripe--flame" style="left:0;width:22px"></div>
    <div class="stripe stripe--ember" style="left:22px;width:22px"></div>
    <div class="stripe stripe--ember" style="left:473px;width:22px"></div>
    <div class="stripe stripe--flame" style="left:495px;width:22px"></div>
    <div class="wordmark"><span class="mark-square"></span>Tranvik<br>Leasing Corp</div>
  </section>

  <section class="card card--back" aria-label="Card back">
    <div class="stripe stripe--flame" style="left:0;width:11px"></div>
    <div class="stripe stripe--ember" style="left:11px;width:8px"></div>
    <div class="back-brand">
      <div class="wordmark"><span class="mark-square"></span>Tranvik<br>Leasing Corp</div>
    </div>
    <div class="rule"></div>
    <p class="web">www.tranvikleasing.ca</p>
    <div class="seam"></div>
    <div class="panel">
      <div class="person">
        <p class="person__name">MARA ELLISON</p>
        <p class="person__role">PRESIDENT</p>
      </div>
      <div class="contact">
        <p>403.555.0192</p>
        <p>mara@tranvikleasing.ca</p>
      </div>
    </div>
    <div class="stripe stripe--flame" style="right:0;width:8px"></div>
  </section>
</main>
</body>
</html>
```